Web Design Business Card

I need a new business card designed, we recently rebranded and I need to get a fresh design to match our new logo, colours and branding.

Details:

Dorian Keeble | Founder & CEO
Address: 7 Fernhollow Lane, #04-09 Maplecrest Vale, Singapore 583104
Tel: +65 93468120
Web: www.plumtrove.com.sg
hello@plumtrove.com.sg

I've attached my old card as well

Requirements
Must have
• Front and Back
Interesting use of logo
Correct use of colour scheme

```html
<!DOCTYPE html>
<html lang="en">
<head>
<meta charset="utf-8">
<title>plumtrove – Business Card</title>
<link rel="stylesheet" href="https://fonts.googleapis.com/css2?family=Montserrat:wght@400;600;700&display=swap">
<style>
  :root {
    --stage: #2b2b2c;
    --sky: #5cc1e8;
    --sky-deep: #3fa9d8;
    --paper: #ffffff;
    --paper-shade: #e9e9e9;
    --ink: #6e625c;
    --white: #ffffff;
  }
  * { margin: 0; padding: 0; box-sizing: border-box; }
  html, body {
    width: 1200px; height: 900px; overflow: hidden;
    background: var(--stage);
    font-family: "Montserrat", Arial, sans-serif;
  }
  .canvas {
    position: relative; width: 1200px; height: 900px;
  }
  .card {
    position: absolute; left: 285px; width: 630px; height: 360px;
    box-shadow: 0 14px 40px rgba(0,0,0,.55);
    overflow: hidden;
  }
  /* back side */
  .card--back {
    top: 50px;
    background: linear-gradient(135deg, var(--sky) 0%, var(--sky-deep) 100%);
    display: flex; flex-direction: column; align-items: center; justify-content: center;
  }
  .back-ring {
    width: 200px; height: 200px; border-radius: 50%;
    border: 2px solid rgba(255,255,255,.35);
    box-shadow: inset 0 -6px 14px rgba(0,80,130,.25);
    display: flex; align-items: center; justify-content: center;
  }
  .back-name {
    color: var(--white); font-weight: 700; font-size: 30px; letter-spacing: -0.5px;
  }
  .back-web {
    margin-top: 22px; color: var(--white); font-size: 15px; letter-spacing: .5px;
  }
  /* front side */
  .card--front {
    top: 490px;
    background: linear-gradient(160deg, var(--paper) 0%, var(--paper-shade) 100%);
  }
  .brand {
    position: absolute; left: 48px; top: 48px;
    display: flex; align-items: center; gap: 18px;
  }
  .brand-dot {
    width: 74px; height: 74px; border-radius: 50%;
    background: linear-gradient(160deg, var(--sky), var(--sky-deep));
  }
  .brand-name {
    color: var(--ink); font-weight: 700; font-size: 42px; line-height: 1; letter-spacing: -1px;
  }
  .brand-tagline {
    margin-top: 6px; color: var(--sky-deep); font-weight: 600; font-size: 12px; letter-spacing: 1.2px;
  }
  .person {
    position: absolute; left: 48px; bottom: 62px; color: var(--ink);
  }
  .person-name { font-weight: 600; font-size: 28px; }
  .person-role { font-weight: 600; font-size: 17px; margin-top: 4px; }
  .contact {
    position: absolute; right: 44px; top: 150px; list-style: none;
    color: var(--ink); font-size: 15px; font-weight: 400;
  }
  .contact li {
    display: flex; align-items: flex-start; gap: 10px; margin-bottom: 8px; line-height: 1.45;
  }
  .contact-icon {
    flex: none; width: 22px; height: 22px; margin-top: 0;
  }
</style>
</head>
<body>
<main class="canvas">

  <section class="card card--back" aria-label="Card back">
    <div class="back-ring"><span class="back-name">plumtrove</span></div>
    <p class="back-web">www.plumtrove.com.sg</p>
  </section>

  <section class="card card--front" aria-label="Card front">
    <div class="brand">
      <div class="brand-dot"></div>
      <div>
        <div class="brand-name">plumtrove</div>
        <div class="brand-tagline">WEB DESIGN &amp; CONSULTANCY</div>
      </div>
    </div>

    <div class="person">
      <div class="person-name">Dorian Keeble</div>
      <div class="person-role">Founder &amp; CEO</div>
    </div>

    <ul class="contact">
      <li>
        <svg class="contact-icon" viewBox="0 0 22 22" aria-hidden="true">
          <circle cx="11" cy="11" r="11" fill="var(--sky-deep)"/>
          <path d="M8 6.5l2 2.2-1 1.3c.7 1.3 1.7 2.3 3 3l1.3-1 2.2 2-1.2 1.6c-3.6-.4-7.1-3.9-7.5-7.5z" fill="#fff"/>
        </svg>
        <span>+65 934 681 20</span>
      </li>
      <li>
        <svg class="contact-icon" viewBox="0 0 22 22" aria-hidden="true">
          <circle cx="11" cy="11" r="11" fill="var(--sky-deep)"/>
          <rect x="5.5" y="7.5" width="11" height="7.5" rx="1" fill="#fff"/>
          <path d="M5.8 8l5.2 4 5.2-4" fill="none" stroke="var(--sky-deep)" stroke-width="1.1"/>
        </svg>
        <span>hello@plumtrove.com.sg</span>
      </li>
      <li>
        <svg class="contact-icon" viewBox="0 0 22 22" aria-hidden="true">
          <circle cx="11" cy="11" r="11" fill="var(--sky-deep)"/>
          <path d="M11 5a4 4 0 0 1 4 4c0 3-4 7.5-4 7.5S7 12 7 9a4 4 0 0 1 4-4z" fill="#fff"/>
          <circle cx="11" cy="9" r="1.5" fill="var(--sky-deep)"/>
        </svg>
        <span>7 Fernhollow Lane<br>#04-09 Maplecrest Vale<br>Singapore 583104</span>
      </li>
    </ul>
  </section>

</main>
</body>
</html>
```